Local electrical company needs two flyers designed

We are a small local electrical contracting company and are in desperate need of a awasome flyer design to help grow our business
Updates

hi everyone.

please keep the logo off the front page.
it can go on the rear.

We are really trying to portray a angry/frustrated women BECAUSE her lights are broken.
not light globes

Target Market(s)

Home owners

Industry/Entity Type

Electrical

Font styles to use
Serif

```html
<!DOCTYPE html>
<html lang="en">
<head>
<meta charset="utf-8">
<title>Brightwire Electrical Flyer</title>
<link rel="stylesheet" href="https://fonts.googleapis.com/css2?family=Montserrat:wght@400;700;800&family=Roboto+Condensed:wght@500&family=Roboto:wght@400&display=swap">
<style>
  :root {
    --orange: #e07b1f;
    --ink: #333333;
    --ink-soft: #444444;
    --paper: #ffffff;
    --backdrop: #e6e6e6;
    --rule: #b8b8b8;
    --card-red: #c8102e;
    --card-blue: #1a2a8c;
    --card-plum: #8a1538;
  }
  * { margin: 0; padding: 0; box-sizing: border-box; }
  html, body { width: 1200px; height: 900px; overflow: hidden; background: var(--backdrop); }
  .flyer {
    position: absolute; left: 30px; top: 49px;
    width: 1140px; height: 802px;
    background: var(--paper);
    font-family: "Roboto", Arial, sans-serif;
    color: var(--ink);
  }
  .headline {
    position: absolute; left: 52px; top: 62px;
    font-family: "Montserrat", Arial, sans-serif;
    font-weight: 700; font-size: 122px; line-height: 124px;
    color: var(--orange); letter-spacing: -1px;
  }
  .selling-points {
    position: absolute; left: 54px; top: 322px;
    list-style: none;
    font-family: "Roboto Condensed", "Arial Narrow", sans-serif;
    font-weight: 500; font-size: 34px; line-height: 49.5px;
    color: var(--ink);
  }
  .selling-points li::before { content: "• "; }
  .brand {
    position: absolute; left: 875px; top: 80px; width: 210px;
    text-align: center;
  }
  .brand-art {
    width: 210px; height: 185px;
    background: radial-gradient(circle at 60% 40%, #bfe0f5 0%, #6fae5a 45%, #e07b1f 100%);
    border-radius: 6px;
  }
  .brand-name {
    margin-top: 6px;
    font-family: "Montserrat", Arial, sans-serif;
    font-weight: 800; font-size: 26px; color: var(--orange);
  }
  .testimonial {
    position: absolute; right: 61px; top: 324px; width: 260px;
    text-align: right; font-size: 15.5px; line-height: 17.2px; color: var(--ink-soft);
  }
  .testimonial cite { display: block; margin-top: 16px; font-style: normal; }
  .testimonial cite em { font-style: italic; }
  .payments {
    position: absolute; left: 54px; top: 596px;
    display: flex; gap: 4px; align-items: center;
  }
  .payment-card { width: 56px; height: 35px; border: 1px solid #999; border-radius: 2px; }
  .payment-card.red { background: var(--card-red); }
  .payment-card.blue { background: var(--card-blue); }
  .payment-card.plum { background: var(--card-plum); }
  .credentials {
    margin-left: 12px;
    font-family: "Montserrat", Arial, sans-serif;
    font-weight: 700; font-size: 10px; line-height: 12px;
  }
  .website {
    position: absolute; left: 53px; top: 652px;
    font-family: "Montserrat", Arial, sans-serif;
    font-weight: 700; font-size: 33px; color: var(--ink);
  }
  .fine-print {
    position: absolute; left: 54px; top: 698px;
    font-family: "Montserrat", Arial, sans-serif;
    font-size: 14.5px; line-height: 17px; color: var(--ink-soft);
  }
  .fine-print .indent { padding-left: 9px; }
  .address-panel {
    position: absolute; left: 631px; top: 531px;
    width: 462px; height: 218px;
    border: 1px solid var(--rule);
  }
</style>
</head>
<body>
  <main class="flyer">
    <h1 class="headline">CALL NOW<br>1300 555 208</h1>

    <ul class="selling-points">
      <li>Specialising in domestic electrical repairs</li>
      <li>On Time guarantee or $100 OFF</li>
      <li>Up front pricing</li>
      <li>No mess guaranteed</li>
    </ul>

    <div class="brand">
      <div class="brand-art" role="img" aria-label="Mascot illustration: caped electrician hero holding up a light globe"></div>
      <div class="brand-name">BRIGHTWIRE</div>
    </div>

    <blockquote class="testimonial">
      “Talk about great service!<br>
      I called up to ask about fitting<br>
      a light and they were here<br>
      within half an hour and were<br>
      able to fit it that afternoon.<br>
      Good price and great service.<br>
      I would not hesitate<br>
      to recommend them”
      <cite><em>R.Mason</em> — Ashwood Vale</cite>
    </blockquote>

    <div class="payments">
      <span class="payment-card red" aria-hidden="true"></span>
      <span class="payment-card blue" aria-hidden="true"></span>
      <span class="payment-card plum" aria-hidden="true"></span>
      <p class="credentials">Lic: 480215D<br>ABN: 62 318 904 517</p>
    </div>

    <p class="website">www.brightwirehome.com.au</p>

    <p class="fine-print">
      *Mention this offer when you book your job to receive offer.<br>
      <span class="indent">Limit one per household</span><br>
      *Cannot be combined with any other offer
    </p>

    <div class="address-panel"></div>
  </main>
</body>
</html>
```